Business Cards for 41Vale

I need business cards that goes with the logo
Updates

Dear designers - many thanks for the responsesreceived to date. There are many good designs but most of them are landscape.Could you please submit a few options for portrait layout as well.

Industry/Entity Type

Business

```html
<!DOCTYPE html>
<html lang="en">
<head>
<meta charset="utf-8">
<title>41Vale Business Cards</title>
<link rel="stylesheet" href="https://fonts.googleapis.com/css2?family=Oswald:wght@300;400;600;700&display=swap">
<style>
  :root {
    --brand-red: #e8141b;
    --brand-charcoal: #373c3f;
    --text-grey: #5a5f62;
    --card-border: #3a3a3a;
    --paper: #ffffff;
  }
  * { margin: 0; padding: 0; box-sizing: border-box; }
  html, body {
    width: 1200px;
    height: 1000px;
    overflow: hidden;
    background: var(--paper);
    font-family: "Oswald", "Arial Narrow", sans-serif;
  }
  .card {
    position: absolute;
    width: 700px;
    height: 400px;
    border: 1px solid var(--card-border);
    background: var(--paper);
    overflow: hidden;
  }
  .card--front { left: 249px; top: 69px; }
  .card--back  { left: 252px; top: 541px; }

  .top-band {
    position: absolute;
    left: 0; top: 0;
    width: 595px;
    height: 24px;
    background: var(--brand-red);
    border-bottom-right-radius: 8px;
  }
  .web-tab {
    position: absolute;
    right: 0; bottom: 0;
    width: 293px;
    height: 27px;
    background: var(--brand-charcoal);
    border-top-left-radius: 8px;
    color: var(--paper);
    font-weight: 600;
    font-size: 17px;
    line-height: 27px;
    letter-spacing: 0.3px;
    padding-left: 92px;
  }

  .wordmark {
    position: absolute;
    display: flex;
    align-items: center;
    color: var(--brand-charcoal);
    font-weight: 600;
    line-height: 1;
  }
  .wordmark__dot {
    border-radius: 50%;
    background: var(--brand-red);
    flex: none;
  }
  .card--front .wordmark {
    left: 0; right: 0; top: 120px;
    justify-content: center;
    font-size: 128px;
    gap: 22px;
  }
  .card--front .wordmark__dot { width: 40px; height: 40px; }

  .card--back .wordmark {
    left: 0; width: 349px; top: 150px;
    justify-content: center;
    font-size: 76px;
    gap: 14px;
  }
  .card--back .wordmark__dot { width: 24px; height: 24px; }

  .divider {
    position: absolute;
    left: 349px; top: 68px;
    width: 3px; height: 264px;
    background: var(--brand-charcoal);
  }

  .contact {
    position: absolute;
    left: 432px; top: 86px;
    color: var(--text-grey);
  }
  .contact__name {
    color: var(--brand-charcoal);
    font-weight: 600;
    font-size: 19px;
    line-height: 26px;
    margin-bottom: 20px;
  }
  .contact__address {
    font-weight: 300;
    font-size: 16px;
    line-height: 23.5px;
    font-style: normal;
    margin-bottom: 16px;
  }
  .contact__lines {
    list-style: none;
    font-weight: 300;
    font-size: 16px;
    line-height: 24px;
  }
  .contact__label {
    display: inline-block;
    width: 36px;
    color: var(--brand-red);
    font-weight: 600;
  }
  .contact__label--wide { width: auto; margin-right: 4px; }
</style>
</head>
<body>

  <section class="card card--front" aria-label="Business card front">
    <div class="top-band"></div>
    <div class="wordmark">
      <span class="wordmark__text">41Vale</span>
      <span class="wordmark__dot"></span>
    </div>
    <div class="web-tab">www.41vale.co.za</div>
  </section>

  <section class="card card--back" aria-label="Business card back">
    <div class="top-band"></div>
    <div class="wordmark">
      <span class="wordmark__text">41Vale</span>
      <span class="wordmark__dot"></span>
    </div>
    <div class="divider"></div>
    <div class="contact">
      <p class="contact__name">Johan de Villiers</p>
      <address class="contact__address">
        PO Box 47219<br>
        Kloofendal Ridge<br>
        0187<br>
        South Africa
      </address>
      <ul class="contact__lines">
        <li><span class="contact__label">Tel</span><span class="contact__label" style="width:12px">:</span>+27 82 514 7263</li>
        <li><span class="contact__label">Fax</span><span class="contact__label" style="width:12px">:</span>+27 86 309 4158</li>
        <li><span class="contact__label contact__label--wide">Email :</span>johan@41vale.co.za</li>
      </ul>
    </div>
    <div class="web-tab">www.41vale.co.za</div>
  </section>

</body>
</html>
```